Speisekarten-Design für SportsBar
Zielgruppe
Wir sind moderne SportsBar eines 2.Bundesligisten mit breitem Publikum auch ausserhalb der Fussballs. Wir haben Salate, Burger, Schnitzel und Steaks sowie eine gut sortierte Getränkekarte.
Aufgabenstellung
Für unsere Restaurant Ahornstube SportsBar suchen wir eine neue Speisekarte (Alte Speisekarte ist angehängt)
Wir haben uns für das Format A4 im Clipboard entschieden, da wir flexibel sein möchten, auch wenn sich mal etwas ändern sollte, wir somit eine Seite austauschen können. Auch wollen wir mit einer Wochenkarte arbeiten, die auf der zweiten Seite anhängen sollte.
Wir wünschen uns ein sportlich modernes Design, mit Speisefotos und Sportfotos im Mix als Eyecatcher.
Die Seite für den Kaffe wird nicht benötigt, da wir diese von unserem Partner als fertige Vorlage bekommen(Seite hängt an).
Logos der Getränkemarken sind ebenfalls im Anhang. Aller anderen Fotos etc. können sofort bei Bedarf geliefert werden.
Für den ersten Entwurf würde ich gerne 3-5 Seiten sehen wollen, dabei sind wichtig !
- Titelseite
- Brunch & Buffetseite
- Schnitzelseite
- Burgerseite
- Getränke(Bier)
Vielen Dank, für fragen stehe ich jederzeit zur Verfügung

```html
<!DOCTYPE html>
<html lang="de">
<head>
<meta charset="UTF-8">
<title>Wochen-Angebot</title>
<link rel="stylesheet" href="https://fonts.googleapis.com/css2?family=Carlito:wght@400;700&display=swap">
<style>
  :root {
    --grass-dark: #3b5878;
    --grass-mid: #5c7ea3;
    --grass-light: #7f9cbd;
    --panel: rgba(238, 239, 243, 0.96);
    --ink: #1b1b1b;
  }
  * { margin: 0; padding: 0; box-sizing: border-box; }
  html, body { width: 848px; height: 1200px; overflow: hidden; }
  body {
    font-family: "Carlito", "Calibri", sans-serif;
    color: var(--ink);
  }
  .page {
    position: relative;
    width: 848px;
    height: 1200px;
    overflow: hidden;
  }
  .grass-backdrop {
    position: absolute;
    inset: 0;
    background:
      radial-gradient(ellipse at 30% 20%, var(--grass-light) 0%, transparent 60%),
      radial-gradient(ellipse at 75% 80%, var(--grass-mid) 0%, transparent 65%),
      linear-gradient(180deg, var(--grass-mid) 0%, var(--grass-dark) 100%);
  }
  .menu-panel {
    position: absolute;
    left: 40px;
    top: 40px;
    width: 767px;
    height: 1119px;
    border-radius: 14px;
    background: var(--panel);
  }
  .menu-title {
    position: absolute;
    top: 43px;
    left: 0;
    width: 100%;
    text-align: center;
    font-size: 28px;
    font-weight: 700;
    line-height: 1;
  }
  .offer {
    position: absolute;
    left: 0;
    width: 100%;
    height: 170px;
  }
  .offer p {
    position: absolute;
    left: 0;
    width: 100%;
    text-align: center;
    line-height: 1;
    white-space: nowrap;
  }
  .offer-intro { top: -8.5px; font-size: 17px; }
  .dish-name  { top: 34px;   font-size: 21px; }
  .dish-side  { top: 58.5px; font-size: 17px; }
  .dish-salad { top: 99.5px; font-size: 17px; }
  .dish-price { top: 142px;  font-size: 20px; }
</style>
</head>
<body>
  <main class="page">
    <div class="grass-backdrop" role="img" aria-label="Foto eines Rasens in kühlen Blautönen als Hintergrund"></div>
    <section class="menu-panel">
      <h1 class="menu-title">Wochen-Angebot</h1>

      <article class="offer" style="top:143px">
        <p class="offer-intro">Diese Woche gibt es bei uns was wahnsinnig leckeres:</p>
        <p class="dish-name">Beispiel-Hauptgericht</p>
        <p class="dish-side">mit Beispiel-Beilage</p>
        <p class="dish-salad">auf Wunsch mit Beispielsalat</p>
        <p class="dish-price">12,80€</p>
      </article>

      <article class="offer" style="top:388px">
        <p class="offer-intro">Diese Woche gibt es bei uns was wahnsinnig leckeres:</p>
        <p class="dish-name">Beispiel-Hauptgericht</p>
        <p class="dish-side">mit Beispiel-Beilage</p>
        <p class="dish-salad">auf Wunsch mit Beispielsalat</p>
        <p class="dish-price">12,80€</p>
      </article>

      <article class="offer" style="top:632px">
        <p class="offer-intro">Diese Woche gibt es bei uns was wahnsinnig leckeres:</p>
        <p class="dish-name">Beispiel-Hauptgericht</p>
        <p class="dish-side">mit Beispiel-Beilage</p>
        <p class="dish-salad">auf Wunsch mit Beispielsalat</p>
        <p class="dish-price">12,80€</p>
      </article>
    </section>
  </main>
</body>
</html>
```